Sheep ranch business card design

We need a business card design for our farm. We do all things sheep. We run Babydoll southdown sheep and use their fiber and meat. In the spring the lambs are sold. We shear them for their wool to make dryer balls, roving, and yarn which we sell. We also lease the sheep out to organic vineyards in the winter time to help them convert their weeds and cover crops to manure so they don't have to use tractors and tillers to mow and compact soil. Copperfield Ranch also breeds Kangals which are livestock guard dogs that live with and protect the sheep. We also run a small herd of jersey cows, chickens, and bees but the sheep enterprise is the focal point. I would like to see the design use more earth tones and natural colors and have the feel of a modern and hip farm. I would also like our attached copperfield ranch image to be used. The font family is dalle for our logo. That font can be used or something to compliment it. The attached pictures can be used as well but they are not necessary. One copperfield ranch upload is in psd and one is in jpeg. Thank You and we look forward to seeing your work.
Updates

So many great designs. Not looking for anything "western." Font, design, or otherwise.

Industry/Entity Type

Livestock

Contact Information for Business Card

Copperfield Ranch
Tessa Pollard
www.copperfieldranch.example
copperfieldranch@mailbox.example
phone: 555 210-7389

```html
<!DOCTYPE html>
<html lang="en">
<head>
<meta charset="utf-8">
<title>Copperfield Ranch – Business Card</title>
<link href="https://fonts.googleapis.com/css2?family=Questrial&display=swap" rel="stylesheet">
<style>
  :root {
    --backdrop: #2b2b2d;
    --card-white: #f4f4f3;
    --ink: #4a4a4c;
    --rule: #6d6d70;
    --sepia-light: #d9a56f;
    --sepia-mid: #a8763f;
    --sepia-dark: #5e4124;
    --frame-light: #f3ede4;
  }
  * { margin: 0; padding: 0; box-sizing: border-box; }
  html, body {
    width: 1200px;
    height: 900px;
    overflow: hidden;
    background: var(--backdrop);
    font-family: "Questrial", sans-serif;
  }
  .sheet {
    width: 1200px;
    height: 900px;
    display: flex;
    flex-direction: column;
    align-items: center;
    justify-content: center;
    gap: 40px;
  }
  .card {
    position: relative;
    width: 700px;
    height: 400px;
    overflow: hidden;
    box-shadow: 0 10px 30px rgba(0,0,0,0.45);
  }
  .card-back-photo {
    position: absolute;
    inset: 0;
    background:
      radial-gradient(ellipse at 60% 45%, var(--sepia-light) 0%, var(--sepia-mid) 55%, var(--sepia-dark) 100%);
  }
  .card-frame {
    position: absolute;
    inset: 22px;
    border: 1.5px solid var(--frame-light);
  }
  .card-front .card-frame {
    border-color: var(--rule);
    border-width: 1px;
  }
  .brand {
    display: flex;
    align-items: center;
    justify-content: center;
    gap: 18px;
    font-size: 46px;
    letter-spacing: 0.16em;
    text-transform: uppercase;
  }
  .brand-dot {
    width: 22px;
    height: 22px;
    border-radius: 50%;
    background: currentColor;
  }
  .card-back .brand {
    position: absolute;
    left: 0; right: 0;
    top: 170px;
    color: var(--frame-light);
  }
  .card-front {
    background: var(--card-white);
    color: var(--ink);
  }
  .card-front .brand {
    position: absolute;
    left: 0; right: 0;
    top: 74px;
  }
  .contact-block {
    position: absolute;
    left: 0; right: 0;
    top: 170px;
    text-align: center;
  }
  .person-name {
    display: inline-block;
    font-size: 25px;
    letter-spacing: 0.06em;
    text-transform: uppercase;
    padding: 0 10px 8px;
    border-bottom: 1px solid var(--rule);
    width: 250px;
  }
  .contact-lines {
    list-style: none;
    margin-top: 12px;
    font-size: 17px;
    line-height: 1.45;
    letter-spacing: 0.03em;
  }
</style>
</head>
<body>
  <main class="sheet">
    <section class="card card-back">
      <div class="card-back-photo" role="img" aria-label="Sepia-toned close-up photograph of a woolly sheep in a pasture"></div>
      <div class="card-frame"></div>
      <div class="brand"><span>Copperfield</span><span class="brand-dot"></span><span>Ranch</span></div>
    </section>

    <section class="card card-front">
      <div class="card-frame"></div>
      <div class="brand"><span>Copperfield</span><span class="brand-dot"></span><span>Ranch</span></div>
      <div class="contact-block">
        <div class="person-name">Tessa Pollard</div>
        <ul class="contact-lines">
          <li>555 210-7389</li>
          <li>copperfieldranch@mailbox.example</li>
          <li>www.copperfieldranch.example</li>
        </ul>
      </div>
    </section>
  </main>
</body>
</html>
```